we are a college and require a design of a printable graduation certificate

our courses range from certicate III to Diploma

We would a high quality design, similar to a unveristy degree, so its meaning full to the students and looks great on the wall

our college website is: www.marlowinstitute.example.au

Industry/Entity Type

College

Requirements
Must have
• security feature like water mark or stamp

```html
<!DOCTYPE html>
<html lang="en">
<head>
<meta charset="utf-8">
<title>Marlow Institute – Certificate of Graduation</title>
<link rel="stylesheet" href="https://fonts.googleapis.com/css2?family=Dancing+Script:wght@700&family=Questrial&display=swap">
<style>
  :root {
    --frame-black: #000000;
    --paper: #ffffff;
    --vine-light: #eeeff1;
    --vine-mid: #c9ccd1;
    --ink: #555555;
    --ink-dark: #2a2a2a;
    --rule: #4a4a4a;
    --crest-blue: #1f4fe0;
    --seal-red: #b3191b;
    --seal-dark: #8a1012;
  }
  * { box-sizing: border-box; margin: 0; padding: 0; }
  html, body { width: 1200px; height: 855px; overflow: hidden; background: var(--frame-black); }
  .certificate {
    position: relative;
    width: 1200px;
    height: 855px;
    background: var(--frame-black);
    font-family: "Questrial", sans-serif;
    color: var(--ink);
  }
  .sheet {
    position: absolute;
    left: 78px; top: 52px;
    width: 1044px; height: 738px;
    background: var(--paper);
  }
  .vine-border {
    position: absolute;
    inset: 0;
    background: linear-gradient(135deg, var(--vine-mid), var(--vine-light) 50%, var(--vine-mid));
  }
  .sheet-inner {
    position: absolute;
    left: 40px; top: 42px; right: 40px; bottom: 40px;
    background: var(--paper);
  }
  .content { position: absolute; inset: 0; }
  .brand {
    position: absolute;
    left: 0; right: 0; top: 268px;
    display: flex; justify-content: center; align-items: center; gap: 14px;
  }
  .brand-mark {
    width: 26px; height: 26px; border-radius: 50%;
    background: var(--crest-blue);
  }
  .brand-name {
    font-size: 30px;
    letter-spacing: 1px;
    color: var(--ink-dark);
  }
  .title {
    position: absolute;
    left: 0; right: 0; top: 352px;
    text-align: center;
    font-family: "Dancing Script", cursive;
    font-weight: 700;
    font-size: 60px;
    color: var(--ink);
  }
  .line-text {
    position: absolute;
    left: 0; right: 0;
    text-align: center;
    font-size: 31px;
    line-height: 1;
  }
  .certify { top: 452px; }
  .course { top: 545px; }
  .on { top: 632px; font-size: 27px; }
  .rule {
    position: absolute;
    height: 1px;
    background: var(--rule);
  }
  .rule-name { left: 226px; width: 752px; top: 515px; }
  .rule-course { left: 217px; width: 751px; top: 607px; }
  .rule-date { left: 243px; width: 715px; top: 684px; }
  .field {
    position: absolute; top: 708px;
    font-size: 23px; color: var(--ink-dark);
  }
  .field-name { left: 175px; }
  .field-signature { left: 478px; }
  .field-date { left: 818px; }
  .dots {
    position: absolute; top: 728px;
    border-bottom: 2px dotted var(--ink-dark);
  }
  .dots-name { left: 257px; width: 202px; }
  .dots-signature { left: 597px; width: 202px; }
  .dots-date { left: 880px; width: 143px; }
  .seal {
    position: absolute;
    left: 975px; top: 588px;
    width: 98px; height: 98px; border-radius: 50%;
    background: radial-gradient(circle at 40% 35%, var(--seal-red), var(--seal-dark));
  }
</style>
</head>
<body>
  <main class="certificate">
    <div class="sheet">
      <div class="vine-border" role="img" aria-label="Silver leaf and vine ornamental border"></div>
      <div class="sheet-inner"></div>
    </div>
    <div class="content">
      <div class="brand">
        <span class="brand-mark"></span>
        <span class="brand-name">MARLOW INSTITUTE</span>
      </div>
      <h1 class="title">Certificate of Graduation</h1>
      <p class="line-text certify">This is to Certify that</p>
      <div class="rule rule-name"></div>
      <p class="line-text course">has Completed a&nbsp; course of study in</p>
      <div class="rule rule-course"></div>
      <p class="line-text on">on</p>
      <div class="rule rule-date"></div>
      <span class="field field-name">Name</span>
      <span class="dots dots-name"></span>
      <span class="field field-signature">Signature</span>
      <span class="dots dots-signature"></span>
      <span class="field field-date">Date</span>
      <span class="dots dots-date"></span>
      <div class="seal" role="img" aria-label="Red wax seal with ribbon"></div>
    </div>
  </main>
</body>
</html>
```